Brickline Rentals podcast postcard

I've launched a podcast about apartment investing, ownership and management which is newly up on orbix and wavlino. I want to create a postcard that I can mail to my client base to get them to subscribe

```html
<!DOCTYPE html>
<html lang="en">
<head>
<meta charset="utf-8">
<title>Brickline Rentals Podcast Postcard</title>
<link href="https://fonts.googleapis.com/css2?family=Montserrat:wght@400;500;600;700;800;900&display=swap" rel="stylesheet">
<style>
  :root {
    --blue: #1d5d95;
    --blue-light: #9bc0de;
    --orange: #f7941d;
    --orange-deep: #d97508;
    --ink: #1b1b1b;
    --paper: #ffffff;
    --backdrop: #efefef;
    --stamp: #e6e6e6;
    --rule: #9a9a9a;
  }
  * { box-sizing: border-box; margin: 0; padding: 0; }
  html, body { width: 783px; height: 1200px; overflow: hidden; }
  body {
    background: var(--backdrop);
    font-family: "Montserrat", sans-serif;
    position: relative;
  }
  .postcard {
    position: absolute;
    left: 26px;
    width: 730px;
    height: 486px;
    background: var(--paper);
    box-shadow: 0 2px 8px rgba(0,0,0,.18);
    overflow: hidden;
  }
  .postcard--front { top: 70px; }
  .postcard--back { top: 630px; }
  .postcard svg.shapes { position: absolute; inset: 0; }

  /* brand name block */
  .brand { position: absolute; display: flex; align-items: center; gap: 8px; color: var(--blue); font-weight: 700; }
  .brand__square { width: 12px; height: 12px; background: var(--orange); flex: none; }
  .brand__name { line-height: 1.05; letter-spacing: .5px; }
  .brand__name span { display: block; }
  .front-brand { left: 34px; top: 40px; font-size: 22px; }
  .back-brand { left: 414px; top: 48px; font-size: 14px; }

  /* front headline */
  .headline {
    position: absolute; left: 30px; top: 136px;
    color: var(--paper); font-weight: 900; font-size: 42px; line-height: 1.04; letter-spacing: .5px;
  }
  .headline-rule { position: absolute; left: 32px; top: 228px; width: 84px; height: 3px; background: var(--paper); }

  /* service strip */
  .service { position: absolute; top: 346px; display: flex; align-items: center; gap: 14px; color: var(--paper); font-weight: 800; font-size: 22px; letter-spacing: .3px; }
  .service__badge { width: 50px; height: 50px; border-radius: 50%; background: var(--paper); border: 4px solid var(--blue); flex: none; }
  .service--investing { left: 30px; }
  .service--owning { left: 278px; }
  .service--managing { left: 500px; }
  .strip-divider { position: absolute; top: 355px; height: 30px; border-left: 1.5px dashed rgba(255,255,255,.7); }

  /* contact line */
  .contact { position: absolute; font-weight: 700; color: var(--ink); display: flex; align-items: center; white-space: nowrap; }
  .contact__label { color: var(--blue); margin-right: 8px; }
  .front-call { left: 27px; top: 430px; font-size: 20px; letter-spacing: .5px; }
  .front-web { left: 470px; top: 430px; font-size: 20px; letter-spacing: .8px; gap: 12px; }
  .globe { width: 22px; height: 22px; flex: none; }

  /* back */
  .photo { position: absolute; top: 24px; width: 148px; height: 104px; border: 2px solid var(--paper); }
  .photo--bedroom { left: 28px; background: linear-gradient(160deg, #6f6a64 0%, #c9c2b6 50%, #3b3733 100%); }
  .photo--lounge { left: 194px; background: linear-gradient(170deg, #2b3d52 0%, #7a93a8 45%, #d8d2c6 75%, #3a3a3a 100%); }
  .back-title { position: absolute; left: 28px; top: 142px; font-size: 19px; font-weight: 800; color: var(--paper); letter-spacing: .3px; }
  .back-title em { font-style: normal; color: var(--orange); }
  .back-title-rule { position: absolute; left: 28px; top: 172px; width: 30px; height: 2px; background: var(--paper); }
  .back-intro { position: absolute; left: 28px; top: 186px; width: 320px; font-size: 9.6px; line-height: 1.3; color: var(--paper); }
  .feature { position: absolute; width: 150px; display: flex; gap: 10px; font-size: 9.6px; line-height: 1.3; color: var(--paper); }
  .feature svg { width: 16px; height: 12px; flex: none; margin-top: 1px; }
  .feature--a { left: 28px; top: 284px; }
  .feature--b { left: 190px; top: 284px; }
  .feature--c { left: 28px; top: 333px; }
  .feature--d { left: 190px; top: 333px; }
  .back-call { left: 28px; top: 410px; font-size: 18px; letter-spacing: .5px; }
  .back-web { left: 28px; top: 442px; font-size: 17px; letter-spacing: .8px; gap: 12px; }
  .back-web .globe { width: 20px; height: 20px; }
  .follow { display: flex; align-items: center; gap: 8px; margin-left: 14px; padding-left: 14px; border-left: 1px dashed #777; font-size: 11px; font-weight: 500; letter-spacing: .5px; }
  .follow strong { color: var(--blue); font-weight: 700; }
  .stamp-box { position: absolute; left: 608px; top: 30px; width: 92px; height: 92px; background: var(--stamp); }
  .address-line { position: absolute; left: 414px; width: 288px; height: 1px; background: var(--rule); }
</style>
</head>
<body>

<section class="postcard postcard--front" aria-label="Postcard front">
  <svg class="shapes" viewBox="0 0 730 486" width="730" height="486">
    <defs>
      <linearGradient id="buildingTones" x1="0" y1="0" x2="0" y2="1">
        <stop offset="0" stop-color="#c9ced3"/>
        <stop offset=".35" stop-color="#e8ebee"/>
        <stop offset=".6" stop-color="#7d95b8"/>
        <stop offset="1" stop-color="#3f7d2f"/>
      </linearGradient>
      <linearGradient id="stripFade" x1="0" y1="0" x2="0" y2="1">
        <stop offset="0" stop-color="#f7941d"/>
        <stop offset=".65" stop-color="#f7941d"/>
        <stop offset="1" stop-color="#d97508"/>
      </linearGradient>
    </defs>
    <polyline points="0,114 333,114 496,23" fill="none" stroke="#f7941d" stroke-width="3"/>
    <polygon points="508,24 572,24 730,128 730,150 690,136" fill="#f7941d"/>
    <polygon role="img" aria-label="Photo of a modern white apartment tower with blue balconies among trees" points="306,328 306,118 338,118 496,32 684,140 730,156 730,328" fill="url(#buildingTones)"/>
    <rect x="0" y="118" width="301" height="210" fill="#1d5d95"/>
    <rect role="img" aria-label="Light blue city skyline silhouette" x="0" y="250" width="301" height="78" fill="#9bc0de"/>
    <rect x="0" y="333" width="730" height="78" fill="url(#stripFade)"/>
    <rect x="0" y="413" width="730" height="4" fill="#1d5d95"/>
  </svg>

  <div class="brand front-brand">
    <div class="brand__square"></div>
    <div class="brand__name"><span>BRICKLINE</span><span>RENTALS</span></div>
  </div>

  <h1 class="headline">BRICKLINE<br>PODCAST</h1>
  <div class="headline-rule"></div>

  <div class="service service--investing"><div class="service__badge"></div>INVESTING</div>
  <div class="strip-divider" style="left:237px"></div>
  <div class="service service--owning"><div class="service__badge"></div>OWNING</div>
  <div class="strip-divider" style="left:470px"></div>
  <div class="service service--managing"><div class="service__badge"></div>MANAGING</div>

  <div class="contact front-call"><span class="contact__label">SUBSCRIBE ON:</span>ORBIX &amp; WAVLINO</div>
  <div class="contact front-web">
    <svg class="globe" viewBox="0 0 24 24" fill="none" stroke="#1d5d95" stroke-width="2"><circle cx="12" cy="12" r="10"/><ellipse cx="12" cy="12" rx="4.5" ry="10"/><line x1="2" y1="12" x2="22" y2="12"/><line x1="4" y1="7" x2="20" y2="7"/><line x1="4" y1="17" x2="20" y2="17"/></svg>
    www.brickline.fm
  </div>
</section>

<section class="postcard postcard--back" aria-label="Postcard back">
  <svg class="shapes" viewBox="0 0 730 486" width="730" height="486">
    <defs>
      <linearGradient id="featureFade" x1="0" y1="0" x2="0" y2="1">
        <stop offset="0" stop-color="#f7941d"/>
        <stop offset=".7" stop-color="#f7941d"/>
        <stop offset="1" stop-color="#d97508"/>
      </linearGradient>
    </defs>
    <rect x="0" y="0" width="367" height="397" fill="#1d5d95"/>
    <polygon points="0,253 367,253 367,241 380,253 380,385 0,385" fill="url(#featureFade)"/>
  </svg>

  <div class="photo photo--bedroom" role="img" aria-label="Photo of a bright apartment bedroom"></div>
  <div class="photo photo--lounge" role="img" aria-label="Photo of a living room with tall city-view windows"></div>

  <h2 class="back-title">BRICKLINE <em>PODCAST</em></h2>
  <div class="back-title-rule"></div>
  <p class="back-intro">Brickline Rentals now has a podcast. Each week we talk apartment investing, ownership and property management with owners, lenders and managers. New episodes drop every Tuesday, so subscribe free on Orbix or Wavlino and never miss a show.</p>

  <div class="feature feature--a"><svg viewBox="0 0 16 12" fill="none" stroke="#fff" stroke-width="1.4"><polyline points="1,8 8,2 15,8"/><polyline points="4,11 8,7 12,11"/></svg><span>Investing tips to size up your next apartment deal</span></div>
  <div class="feature feature--b"><svg viewBox="0 0 16 12" fill="none" stroke="#fff" stroke-width="1.4"><polyline points="1,8 8,2 15,8"/><polyline points="4,11 8,7 12,11"/></svg><span>Ownership stories from owners who built portfolios</span></div>
  <div class="feature feature--c"><svg viewBox="0 0 16 12" fill="none" stroke="#fff" stroke-width="1.4"><polyline points="1,8 8,2 15,8"/><polyline points="4,11 8,7 12,11"/></svg><span>Management advice for tenants, repairs and rent</span></div>
  <div class="feature feature--d"><svg viewBox="0 0 16 12" fill="none" stroke="#fff" stroke-width="1.4"><polyline points="1,8 8,2 15,8"/><polyline points="4,11 8,7 12,11"/></svg><span>New episodes weekly, free on Orbix and Wavlino</span></div>

  <div class="contact back-call"><span class="contact__label">SUBSCRIBE ON:</span>ORBIX &amp; WAVLINO</div>
  <div class="contact back-web">
    <svg class="globe" viewBox="0 0 24 24" fill="none" stroke="#1d5d95" stroke-width="2"><circle cx="12" cy="12" r="10"/><ellipse cx="12" cy="12" rx="4.5" ry="10"/><line x1="2" y1="12" x2="22" y2="12"/><line x1="4" y1="7" x2="20" y2="7"/><line x1="4" y1="17" x2="20" y2="17"/></svg>
    www.brickline.fm
    <span class="follow">follow us <strong>Pictora</strong></span>
  </div>

  <div class="brand back-brand">
    <div class="brand__square"></div>
    <div class="brand__name"><span>BRICKLINE</span><span>RENTALS</span></div>
  </div>
  <div class="stamp-box"></div>
  <div class="address-line" style="top:215px"></div>
  <div class="address-line" style="top:255px"></div>
  <div class="address-line" style="top:293px"></div>
  <div class="address-line" style="top:330px"></div>
</section>

</body>
</html>
```